Corewise Motion Business Cards

Can all designers please apply the following info on their designs' back-side of the business card: (please see brief file upload ('Info for backside...' - for required info, colours & layout)

SPECIALISING IN INDIVIDUAL PILATES INSTRUCTION
MATWORK – including small apparatus
and STUDIO:
VIVANTE 5 REFORMER
LADDER BARREL
MERIDAN BARREL
TENDRA DOME
KALVO CHAIR
TOR-I-VAN

Business Cards for Corewise Motion - applying the Corewise Motion logo design selected earlier.
Note the business card requires both a front and back side. Please refer to two uploaded ppt-files for type of info required to be displayed, and rough position of where info could be. Require innovative / fresh approach to business card design and use of colour by designers now. Please refer to and use logo as uploaded - also for potential business card colour application.

Dear Designers,

Please note the additional inclusion / upload of two draft ppt-files that try to show where I want what type of information, for both the front & back sides of the required business card, plus an attempt at showing the high-level concept / idea of business info position.

As my 'drafts' obviously lack colour and any ability towards innovative card design or approach – I now rely on your vastly superior graphic design abilities to produce a really great business card for my business…

Looking forward to your submissions!

Kind regards, Maren for: Corewise Motion 

Hello all Designers,

Can all designers please apply the following info on their designs' back-side of the business card: (please see / refer to the Brief and specifically the file upload ('Info for backside...' - for required info, colours & layout) - for the backside of the business card).

Info content (without colour, layout etc.):

and STUDIO:

VIVANTE 5 REFORMER

LADDER BARREL

MERIDAN BARREL

TENDRA DOME

KALVO CHAIR

TOR-I-VAN

Thank you to all designers that submitted for consideration!

With regards,

Corewise Motion

```html
<!DOCTYPE html>
<html lang="en">
<head>
<meta charset="utf-8">
<title>Corewise Motion – Business Card</title>
<link rel="stylesheet" href="https://fonts.googleapis.com/css2?family=Roboto+Condensed:ital,wght@0,400;0,700;1,700&family=Arimo:ital,wght@0,400;1,400&display=swap">
<style>
  :root {
    --orange: #e0522a;
    --green: #3f6a2c;
    --list-grey: #4e5a44;
    --ink: #1e1e1e;
    --card: #ffffff;
    --backdrop: #e7e7e5;
  }
  * { box-sizing: border-box; margin: 0; padding: 0; }
  html, body { width: 1200px; height: 1000px; overflow: hidden; }
  body { background: var(--backdrop); position: relative; font-family: "Arimo", Arial, sans-serif; }

  .card {
    position: absolute;
    width: 820px;
    height: 470px;
    background: var(--card);
    box-shadow: 0 6px 18px rgba(0,0,0,0.18);
    overflow: hidden;
  }
  .card__band {
    position: absolute; left: 0; right: 0; bottom: 0;
    height: 22px; background: var(--green);
  }

  /* Back side */
  .card--back { left: 50px; top: 20px; }
  .brand-mark {
    position: absolute; display: flex; align-items: center; gap: 12px;
  }
  .brand-mark__dot { width: 22px; height: 22px; border-radius: 50%; background: var(--green); }
  .card--back .brand-mark { left: 230px; top: 50px; }
  .card--back .brand-mark__name {
    font-family: "Roboto Condensed", sans-serif; font-weight: 400;
    font-size: 40px; color: var(--green);
  }
  .specialty {
    position: absolute; left: 60px; top: 145px;
    font-family: "Roboto Condensed", sans-serif; font-weight: 700;
    font-size: 31px; letter-spacing: 1.5px; color: var(--orange);
  }
  .matwork {
    position: absolute; left: 120px; top: 192px;
    font-family: "Roboto Condensed", sans-serif; font-weight: 700;
    font-size: 22px; letter-spacing: 0.5px; color: var(--green);
  }
  .apparatus {
    position: absolute; left: 300px; top: 228px; list-style: none;
    font-family: "Roboto Condensed", sans-serif; font-weight: 400;
    font-size: 22px; line-height: 31px; letter-spacing: 1px; color: var(--list-grey);
  }
  .apparatus li::before {
    content: ""; display: inline-block; width: 7px; height: 7px; border-radius: 50%;
    background: var(--orange); margin-right: 12px; vertical-align: middle;
  }

  /* Front side */
  .card--front { left: 330px; top: 505px; text-align: center; }
  .card--front .brand-mark { left: 170px; top: 34px; }
  .card--front .brand-mark__name {
    font-family: "Roboto Condensed", sans-serif; font-weight: 400;
    font-size: 60px; color: var(--orange);
  }
  .values {
    position: absolute; left: 0; right: 0; top: 118px;
    display: flex; justify-content: center; gap: 44px;
    font-family: "Roboto Condensed", sans-serif; font-weight: 700; font-style: italic;
    font-size: 28px; letter-spacing: 2px; color: var(--green);
  }
  .values span::before {
    content: ""; display: inline-block; width: 11px; height: 11px; border-radius: 50%;
    background: var(--orange); margin-right: 10px; vertical-align: middle;
  }
  .person { position: absolute; left: 0; right: 0; top: 196px; }
  .person__name {
    font-family: "Roboto Condensed", sans-serif; font-weight: 700;
    font-size: 28px; letter-spacing: 2px; color: var(--orange);
  }
  .person__title { font-style: italic; font-size: 20px; color: var(--ink); margin-top: 2px; }
  .contact {
    position: absolute; left: 0; right: 0; top: 290px;
    font-size: 20px; line-height: 36px; color: var(--ink);
  }
  .contact dt {
    display: inline; font-family: "Roboto Condensed", sans-serif; font-weight: 700;
    color: var(--orange); font-size: 21px;
  }
  .contact dd { display: inline; margin-left: 4px; }
  .contact div { display: block; }
</style>
</head>
<body>

  <section class="card card--back" aria-label="Card back">
    <div class="brand-mark">
      <span class="brand-mark__dot"></span>
      <span class="brand-mark__name">Corewise Motion</span>
    </div>
    <h2 class="specialty">SPECIALISING IN INDIVIDUAL PILATES INSTRUCTION</h2>
    <p class="matwork">MATWORK – including small apparatus and STUDIO:</p>
    <ul class="apparatus">
      <li>VIVANTE 5 REFORMER</li>
      <li>LADDER BARREL</li>
      <li>MERIDAN BARREL</li>
      <li>TENDRA DOME</li>
      <li>KALVO CHAIR</li>
      <li>TOR-I-VAN</li>
    </ul>
    <div class="card__band"></div>
  </section>

  <section class="card card--front" aria-label="Card front">
    <div class="brand-mark">
      <span class="brand-mark__dot"></span>
      <span class="brand-mark__name">Corewise Motion</span>
    </div>
    <p class="values"><span>BALANCE</span><span>STRENGTH</span><span>FLEXIBILITY</span></p>
    <div class="person">
      <h1 class="person__name">MAREN LINDQVIST</h1>
      <p class="person__title">Diploma of Professional Pilates Instruction</p>
    </div>
    <dl class="contact">
      <div><dt>Mobile:</dt><dd>041 555 0187</dd></div>
      <div><dt>Email:</dt><dd>info@corewisemotion.com.au</dd></div>
      <div><dt>Website:</dt><dd>www.corewisemotion.com.au</dd></div>
      <div><dt>Studio Location:</dt><dd>18 Larchmere Road, Ashdale WA 6099</dd></div>
    </dl>
    <div class="card__band"></div>
  </section>

</body>
</html>
```